Political Mail Out Quintero front and back

Front
Esteban (9th Grade) Quintero!

What's that famous saying?

Show me who your friends are and I'll tell you who you really are!
(show the two guys)

Walter Cuellar is charged with voter fraud by changing voter addresses from across the RGV so they could vote in Edinburg
Back
Did Esteban (9th Grade) Quintero commit voter fraud when he ran for office in 2016?
(insert blurred photo)

Here is a list of people from all over the RGV that voted in Edinburg in the 2016 race.
Here is a break down:

(highlight the number and where they were first registered to vote)

9 People voted in Edinburg who were registered in Donna.
13 People voted in Edinburg who were registered in San Juan
8 People voted in Edinburg who were registered in Pharr
31 People voted in Edinburg who were registered in McAllen
2 People voted in Edinburg who were registered in La Joya
6 People voted in Edinburg who were registered in Edcouch
2 People voted in Edinburg who were registered in Mercedes
2 People voted in Edinburg who were registered in Monte Alto
6 People voted in Edinburg who were registered in Weslaco
1 Person voted in Edinburg who were registered in Penitas
3 People voted in Edinburg who were registered in Alamo
5 People voted in Edinburg who were registered in Elsa
6 People voted in Edinburg who were registered in Mission
1 Person voted in Edinburg who were registered in Alton

Will Esteban (9th Grade) Quintero CHEAT in 2020?

Only time will tell.

Vote Esteban (9th Grade) Quintero OUT of office.

```html
<!DOCTYPE html>
<html lang="en">
<head>
<meta charset="utf-8">
<title>Quintero Mail Out – Front and Back</title>
<link rel="stylesheet" href="https://fonts.googleapis.com/css2?family=Anton&family=Montserrat:wght@600;800;900&family=Oswald:wght@500;600;700&family=Kaushan+Script&family=Open+Sans:wght@400&display=swap">
<style>
  :root {
    --navy: #1f3f80;
    --navy-deep: #1c3a78;
    --gold: #f8b61b;
    --orange: #f08b24;
    --white: #ffffff;
    --paper: #ffffff;
  }
  * { box-sizing: border-box; margin: 0; padding: 0; }
  html, body { width: 1200px; height: 839px; overflow: hidden; background: var(--paper); }
  .canvas { position: relative; width: 1200px; height: 839px; }

  /* ---------- Front ---------- */
  .front { position: absolute; left: 67px; top: 62px; width: 505px; height: 714px; overflow: hidden; }
  .front-top { position: absolute; inset: 0 0 auto 0; height: 316px; background: var(--navy); }
  .front-bottom { position: absolute; left: 0; right: 0; top: 316px; bottom: 0;
    background: linear-gradient(180deg, var(--orange) 0%, var(--gold) 45%, var(--gold) 100%); }
  .front-name-first { position: absolute; left: 28px; top: 30px; color: var(--white);
    font-family: "Montserrat", sans-serif; font-weight: 900; font-size: 44px; line-height: 1; white-space: nowrap; }
  .front-name-first .grade { font-family: "Anton", sans-serif; font-weight: 400; font-size: 50px; margin-left: 12px; letter-spacing: -0.5px; }
  .front-name-last { position: absolute; left: 0; width: 505px; top: 78px; text-align: center; color: var(--white);
    font-family: "Anton", sans-serif; font-size: 112px; line-height: 1; transform: scaleY(1.2); transform-origin: top center; letter-spacing: -1px; }
  .saying { position: absolute; left: 78px; top: 240px; color: var(--white); font-family: "Kaushan Script", cursive;
    font-size: 44px; line-height: 1.1; transform: rotate(-9deg); transform-origin: left top; }
  .saying .line2 { display: block; margin-left: 70px; }
  .quote { position: absolute; left: 0; width: 505px; top: 345px; text-align: center; color: var(--navy);
    font-family: "Oswald", sans-serif; font-weight: 600; font-size: 34px; line-height: 1.1; letter-spacing: -0.8px; }
  .friends-photo { position: absolute; left: 2px; top: 430px; width: 450px; height: 284px;
    background: linear-gradient(180deg, #6b5a52 0%, #9a8377 50%, #c9c3bd 100%); border-radius: 60px 60px 0 0; }
  .charge-bubble { position: absolute; left: 287px; top: 427px; width: 198px; height: 198px; border-radius: 50%; background: var(--navy); }
  .charge-text { position: absolute; left: 300px; top: 462px; width: 168px; text-align: right; color: var(--gold);
    font-family: "Montserrat", sans-serif; font-weight: 600; font-size: 12.5px; line-height: 1.3; }
  .charge-text .who { display: block; text-align: center; font-size: 12.5px; }

  /* ---------- Back ---------- */
  .back { position: absolute; left: 631px; top: 62px; width: 505px; height: 714px; background: var(--paper); }
  .back-header { position: absolute; left: 0; top: 0; width: 505px; height: 228px; background: var(--navy); }
  .back-title { position: absolute; left: 22px; top: 22px; color: var(--white); font-family: "Oswald", sans-serif;
    font-weight: 700; line-height: 1; letter-spacing: -1px; }
  .back-title .l1 { display: block; font-size: 44px; white-space: nowrap; }
  .back-title .l1 .name { font-family: "Montserrat", sans-serif; font-weight: 900; font-size: 40px; }
  .back-title .l2 { display: block; font-size: 39px; margin-top: 8px; white-space: nowrap; }
  .back-title .accent { color: var(--gold); }
  .back-question { position: absolute; right: 22px; top: 124px; color: var(--white); font-family: "Oswald", sans-serif;
    font-weight: 700; font-size: 42px; line-height: 1.1; text-align: left; letter-spacing: -1px; }
  .intro { position: absolute; left: 28px; top: 138px; width: 190px; color: var(--white);
    font-family: "Open Sans", sans-serif; font-size: 8.5px; line-height: 1.4; }
  .roll-photo { position: absolute; left: 28px; top: 178px; width: 181px; height: 369px;
    background: linear-gradient(90deg, #c9c9c6 0%, #d8d8d4 60%, #eeeeea 80%, #d6d6d2 100%); }

  .tally { position: absolute; left: 240px; top: 236px; width: 260px; list-style: none; }
  .tally li { display: flex; align-items: center; height: 21.5px; }
  .tally .count { width: 22px; text-align: right; color: var(--navy); font-family: "Anton", sans-serif; font-size: 19px; line-height: 1; }
  .tally .note { width: 88px; margin-left: 3px; color: var(--navy); font-family: "Open Sans", sans-serif; font-size: 7px; line-height: 1.3; }
  .tally .town { margin-left: 6px; color: var(--navy); font-family: "Oswald", sans-serif; font-weight: 700; font-size: 20px; line-height: 1; letter-spacing: -0.5px; }

  .back-close { position: absolute; left: 0; top: 559px; width: 505px; height: 110px; background: var(--navy); }
  .close-question { position: absolute; left: 15px; top: 16px; width: 300px; font-family: "Oswald", sans-serif;
    font-weight: 700; font-size: 29px; line-height: 1.15; letter-spacing: -1px; }
  .close-question .l1 { color: var(--white); display: block; white-space: nowrap; }
  .close-question .l2 { color: var(--gold); display: block; white-space: nowrap; }
  .close-divider { position: absolute; left: 318px; top: 18px; width: 3px; height: 74px; background: var(--gold); }
  .close-answer { position: absolute; left: 332px; top: 18px; width: 160px; text-align: center; color: var(--gold);
    font-family: "Oswald", sans-serif; font-weight: 700; font-size: 33px; line-height: 1.05; letter-spacing: -1px; }
  .back-footer { position: absolute; left: 0; top: 669px; width: 505px; height: 45px; background: var(--gold);
    display: flex; align-items: center; justify-content: center; }
  .back-footer p { color: var(--navy); font-family: "Oswald", sans-serif; font-weight: 700; font-size: 21px; letter-spacing: -0.8px; white-space: nowrap; }
</style>
</head>
<body>
<main class="canvas">

  <section class="front" aria-label="Mail out front">
    <div class="front-top"></div>
    <div class="front-bottom"></div>
    <h1>
      <span class="front-name-first">Esteban<span class="grade">(9TH GRADE)</span></span>
      <span class="front-name-last">QUINTERO!</span>
    </h1>
    <p class="saying">What's that<span class="line2">Famous saying?</span></p>
    <p class="quote">Show me who your friends are and<br>I'll tell YOU WHO YOU REALLY ARE!</p>
    <div class="friends-photo" role="img" aria-label="Photo of two smiling men standing side by side in campaign polo shirts"></div>
    <div class="charge-bubble"></div>
    <p class="charge-text"><span class="who">WALTER CUELLAR</span>is charged with VOTER FRAUD by changing voter addresses from across the RGV so they could vote in Edinburg</p>
  </section>

  <section class="back" aria-label="Mail out back">
    <div class="back-header"></div>
    <h2 class="back-title">
      <span class="l1">Did <span class="name">Esteban</span> (9th Grade)</span>
      <span class="l2">QUINTERO <span class="accent">commit VOTER FRAUD</span></span>
    </h2>
    <p class="back-question">when he ran for<br>office in 2016?</p>
    <p class="intro">Here is a list of people from all over the RGV that voted in Edinburg in the 2016 race.<br>Here is a break down:</p>
    <div class="roll-photo" role="img" aria-label="Blurred photo of a printed voter roll listing addresses and zip codes"></div>

    <ul class="tally">
      <li><span class="count">9</span><span class="note">People voted in Edinburg who were registered in</span><span class="town">Donna</span></li>
      <li><span class="count">13</span><span class="note">People voted in Edinburg who were registered in</span><span class="town">San Juan</span></li>
      <li><span class="count">8</span><span class="note">People voted in Edinburg who were registered in</span><span class="town">Pharr</span></li>
      <li><span class="count">31</span><span class="note">People voted in Edinburg who were registered in</span><span class="town">McAllen</span></li>
      <li><span class="count">2</span><span class="note">People voted in Edinburg who were registered in</span><span class="town">La Joya</span></li>
      <li><span class="count">6</span><span class="note">People voted in Edinburg who were registered in</span><span class="town">Edcouch</span></li>
      <li><span class="count">2</span><span class="note">People voted in Edinburg who were registered in</span><span class="town">Mercedes</span></li>
      <li><span class="count">2</span><span class="note">People voted in Edinburg who were registered in</span><span class="town">Monte Alto</span></li>
      <li><span class="count">6</span><span class="note">People voted in Edinburg who were registered in</span><span class="town">Weslaco</span></li>
      <li><span class="count">1</span><span class="note">People voted in Edinburg who were registered in</span><span class="town">Penitas</span></li>
      <li><span class="count">3</span><span class="note">People voted in Edinburg who were registered in</span><span class="town">Alamo</span></li>
      <li><span class="count">5</span><span class="note">People voted in Edinburg who were registered in</span><span class="town">Elsa</span></li>
      <li><span class="count">6</span><span class="note">People voted in Edinburg who were registered in</span><span class="town">Mission</span></li>
      <li><span class="count">1</span><span class="note">People voted in Edinburg who were registered in</span><span class="town">Alton</span></li>
    </ul>

    <div class="back-close">
      <p class="close-question"><span class="l1">Will Esteban (9th Grade)</span><span class="l2">Quintero CHEAT in 2020?</span></p>
      <div class="close-divider"></div>
      <p class="close-answer">ONLY TIME<br>WILL TELL.</p>
    </div>
    <div class="back-footer"><p>VOTE ESTEBAN (9TH GRADE) QUINTERO OUT OF OFFICE.</p></div>
  </section>

</main>
</body>
</html>
```